Business Card Design for School

We need business cards for our school in Algiers, Algeria.
Our school is a Halvorn Quillset approved centre. (See P2 of attached file).
Our school name is "Ecole Les Brévines" in French and "Brevine School" in English.
We want two-sided cards—one side in English and the other in French.
We want both our school logo and the Halvorn Quillset "approved centre" logo on the cards.
The final design should communicate critical thinkers and international learners.
Thank you.

```html
<!DOCTYPE html>
<html lang="en">
<head>
<meta charset="utf-8">
<title>Brevine School – Business Cards</title>
<link href="https://fonts.googleapis.com/css2?family=Montserrat:wght@400;500;700&family=Oswald:wght@500&display=swap" rel="stylesheet">
<style>
  :root {
    --bg: #5a5a5a;
    --paper: #f4f4f2;
    --orange: #e07a0e;
    --blue: #135f86;
    --badge-blue: #1aa0d2;
    --ink: #3c3c3c;
    --muted: #555555;
  }
  * { box-sizing: border-box; margin: 0; padding: 0; }
  html, body { width: 1200px; height: 900px; overflow: hidden; }
  body {
    background: var(--bg);
    font-family: "Montserrat", Arial, sans-serif;
    color: var(--ink);
  }
  .card-stack {
    position: relative;
    width: 1200px;
    height: 900px;
  }
  .card {
    position: absolute;
    left: 250px;
    width: 700px;
    height: 400px;
    background: var(--paper);
    overflow: hidden;
  }
  .card--english { top: 30px; }
  .card--french { top: 470px; }

  .big-disc {
    position: absolute;
    left: -40px;
    top: 230px;
    width: 460px;
    height: 460px;
    border-radius: 50%;
    background: var(--orange);
  }
  .edge-dot {
    position: absolute;
    right: -45px;
    top: 150px;
    width: 90px;
    height: 90px;
    border-radius: 50%;
    background: var(--orange);
  }

  .person {
    position: absolute;
    left: 48px;
    top: 92px;
  }
  .person__name {
    font-family: "Oswald", "Arial Narrow", sans-serif;
    font-weight: 500;
    font-size: 40px;
    letter-spacing: 0.5px;
    color: var(--orange);
    line-height: 1;
  }
  .person__title {
    margin-top: 8px;
    font-size: 22px;
    color: var(--muted);
    letter-spacing: 1px;
  }

  .brand {
    position: absolute;
    right: 70px;
    top: 42px;
    display: flex;
    align-items: center;
    gap: 18px;
  }
  .brand__disc {
    width: 96px;
    height: 96px;
    border-radius: 50%;
    background: var(--orange);
  }
  .brand__name {
    font-size: 46px;
    font-weight: 700;
    color: var(--blue);
    letter-spacing: 1px;
  }

  .contact {
    position: absolute;
    right: 64px;
    top: 176px;
    text-align: right;
  }
  .contact__school {
    font-size: 20px;
    font-weight: 700;
    color: var(--ink);
    margin-bottom: 10px;
    margin-right: 26px;
  }
  .contact__line {
    display: flex;
    justify-content: flex-end;
    align-items: center;
    gap: 10px;
    font-size: 17px;
    color: var(--muted);
    letter-spacing: 0.5px;
    line-height: 30px;
  }
  .contact__icon { width: 16px; height: 16px; flex: none; }
  .contact__line--plain { margin-right: 26px; }

  .approved {
    position: absolute;
    left: 392px;
    bottom: 42px;
    display: flex;
    align-items: center;
    gap: 10px;
  }
  .approved__mark {
    width: 30px;
    height: 30px;
    border-radius: 50%;
    background: var(--badge-blue);
  }
  .approved__name {
    font-size: 18px;
    font-weight: 500;
    color: var(--ink);
    line-height: 1.1;
  }
  .approved__note {
    font-size: 11px;
    color: var(--muted);
  }
</style>
</head>
<body>
<main class="card-stack">

  <section class="card card--english" aria-label="English side">
    <div class="big-disc" role="img" aria-label="Large school emblem area in orange"></div>
    <div class="edge-dot"></div>
    <div class="person">
      <p class="person__name">SAMIR HADDAD</p>
      <p class="person__title">Director</p>
    </div>
    <div class="brand">
      <div class="brand__disc"></div>
      <span class="brand__name">BREVINE</span>
    </div>
    <div class="contact">
      <p class="contact__school">Brevine School</p>
      <p class="contact__line">021550614 / 021550628
        <svg class="contact__icon" viewBox="0 0 16 16"><path d="M4 1c-1.5 1-2.5 3-1.5 6s4 7 7 8c2 .6 3.5-.3 4.5-1.5l-2.5-2.5-2 1c-1.5-.8-3-2.5-3.7-4l1-2L4 1z" fill="var(--orange)"/></svg>
      </p>
      <p class="contact__line">contact@lesbrevines.com
        <svg class="contact__icon" viewBox="0 0 16 16"><rect x="1" y="3" width="14" height="10" fill="var(--orange)"/><path d="M1 3l7 6 7-6" fill="none" stroke="var(--paper)" stroke-width="1.4"/></svg>
      </p>
      <p class="contact__line contact__line--plain">www.lesbrevines.com</p>
    </div>
    <div class="approved">
      <div class="approved__mark"></div>
      <div>
        <p class="approved__name">Halvorn | Quillset</p>
        <p class="approved__note">Approved Centre</p>
      </div>
    </div>
  </section>

  <section class="card card--french" aria-label="Face en français">
    <div class="big-disc" role="img" aria-label="Grand emblème de l'école en orange"></div>
    <div class="edge-dot"></div>
    <div class="person">
      <p class="person__name">SAMIR HADDAD</p>
      <p class="person__title">Directeur</p>
    </div>
    <div class="brand">
      <div class="brand__disc"></div>
      <span class="brand__name">BREVINE</span>
    </div>
    <div class="contact">
      <p class="contact__school">Ecole Les Brévines</p>
      <p class="contact__line">021550614 / 021550628
        <svg class="contact__icon" viewBox="0 0 16 16"><path d="M4 1c-1.5 1-2.5 3-1.5 6s4 7 7 8c2 .6 3.5-.3 4.5-1.5l-2.5-2.5-2 1c-1.5-.8-3-2.5-3.7-4l1-2L4 1z" fill="var(--orange)"/></svg>
      </p>
      <p class="contact__line">contact@lesbrevines.com
        <svg class="contact__icon" viewBox="0 0 16 16"><rect x="1" y="3" width="14" height="10" fill="var(--orange)"/><path d="M1 3l7 6 7-6" fill="none" stroke="var(--paper)" stroke-width="1.4"/></svg>
      </p>
      <p class="contact__line contact__line--plain">www.lesbrevines.com</p>
    </div>
    <div class="approved">
      <div class="approved__mark"></div>
      <div>
        <p class="approved__name">Halvorn | Quillset</p>
        <p class="approved__note">Approved Centre</p>
      </div>
    </div>
  </section>

</main>
</body>
</html>
```